Counseling Practice Business Card

I need a professional looking business card incorporating my new logo that was just completed. Card needs to incorporate my name and title, description of my specialty, my address, my phone number, my fax number, my email and my website URL. I need to be able to choose design on/with different paper colors and textures.
I do not have a lot of business card ideas so I am open to anything but I want bold,sharp, clear card without additional designs other than my logo (see attached file info). I am open to different color backgrounds or paper colors including black. I do not like traditional brackets around area codes in phone number or dashes between numbers in phone number. Am open to other ways of presenting including periods between numbers as appropriate. I do not know enough to know what I like yet but I want card to coordinate and work together with my logo. My practice emphasizes natural mental health interventions so any use of color (with background paper color or the blue and green in my logo) that elicits nature is nice. In addition to black, any natural brown or wood looking background might be desirable also. Most of the offerings so far look very similar and boring.

Target Market(s)

Potential therapy clients and other professionals

Contact Information for Business Card

Card information:
Marcus T. Whitfield, Ph.D.
Licensed Clinical Psychologist
Integrative Health Coach
4812 Ferndale Pkwy NW
Suite 730
Duluth, GA 30096
(770) 555-0142 phone
(770) 555-0186 fax
drmarcuswhitfield@kelvora.com
pathbloomcounseling.com

Font styles to use
Serif
Sans Serif
Other font styles liked:
• anything that you think looks crisp, clear and easily readable

Requirements
Must have
• Any color used should coordinate with my logo design (see attached files).
• Card should be printed horizontally so top and bottom are longest sides of rectangle.
• Background color or paper color should complement and highlight logo. Do not like a white background. black, grey, brown or any color my logo would blend well with.
Nice to have
• I would like designer to utilize color to highlight letters/name or phone-fax-web symbols.
• Bottom edge of card could be highlighted if appropriate to an idea.
Should not have
• I would NOT want the card to have a pure white background at all.
• No clear cards.
• Cards should be oriented with long sides on bottom and top, NOT sides. DO NOT LIKE THIS THIN TALL ORIENTATION.

```html
<!DOCTYPE html>
<html lang="en">
<head>
<meta charset="utf-8">
<title>Pathbloom Counseling – Business Card</title>
<link rel="stylesheet" href="https://fonts.googleapis.com/css2?family=Oswald:wght@300;400&display=swap">
<style>
  :root {
    --paper: #ffffff;
    --navy: #1f1a3a;
    --slate: #3d4a63;
    --sky: #80c4e2;
    --lime: #b8d12e;
    --brand-blue: #1c75bc;
    --ink-light: #ffffff;
  }
  html, body {
    margin: 0;
    padding: 0;
    width: 1200px;
    height: 703px;
    overflow: hidden;
    background: var(--paper);
  }
  .card {
    position: relative;
    width: 1200px;
    height: 703px;
    overflow: hidden;
    background: var(--paper);
    font-family: "Oswald", "Arial Narrow", sans-serif;
    font-weight: 300;
  }
  .card__backdrop {
    position: absolute;
    inset: 0;
    width: 1200px;
    height: 703px;
  }
  .brand {
    position: absolute;
    left: 72px;
    top: 92px;
    display: flex;
    align-items: center;
    gap: 18px;
    color: var(--brand-blue);
    font-weight: 400;
    font-size: 66px;
    line-height: 1;
    letter-spacing: 1px;
  }
  .brand__dot {
    width: 26px;
    height: 26px;
    border-radius: 50%;
    background: var(--brand-blue);
  }
  .details {
    position: absolute;
    right: 87px;
    top: 272px;
    text-align: right;
    color: var(--ink-light);
  }
  .details__name {
    margin: 0;
    font-size: 46px;
    font-weight: 400;
    line-height: 1.1;
  }
  .details__titles {
    margin: 14px 0 0;
    color: var(--lime);
    font-size: 31px;
    line-height: 1.38;
  }
  .details__address {
    margin: 34px 0 0;
    font-size: 33px;
    line-height: 1.2;
  }
  .sep {
    display: inline-block;
    margin: 0 12px;
  }
  .sep--lime { color: var(--lime); }
  .details__numbers {
    margin: 8px 0 0;
    font-size: 33px;
    line-height: 1.3;
    display: flex;
    justify-content: flex-end;
    align-items: center;
    gap: 34px;
  }
  .number {
    display: inline-flex;
    align-items: center;
    gap: 4px;
  }
  .number__badge {
    display: inline-flex;
    align-items: center;
    justify-content: center;
    width: 34px;
    height: 34px;
    border-radius: 50%;
    background: var(--lime);
    color: var(--navy);
    font-size: 27px;
    font-weight: 400;
    line-height: 1;
  }
  .details__online {
    margin: 30px 0 0;
    font-size: 31px;
    line-height: 1.38;
  }
</style>
</head>
<body>
  <div class="card">
    <svg class="card__backdrop" viewBox="0 0 1200 703" aria-hidden="true">
      <defs>
        <linearGradient id="panelFade" x1="0" y1="0" x2="1" y2="0">
          <stop offset="0" stop-color="#80c4e2"/>
          <stop offset="0.35" stop-color="#4a5a72"/>
          <stop offset="0.7" stop-color="#27253f"/>
          <stop offset="1" stop-color="#1f1a3a"/>
        </linearGradient>
      </defs>
      <path d="M0,290 C480,285 880,190 1200,2 L1200,703 L0,703 Z" fill="var(--lime)"/>
      <path d="M0,299 C490,292 900,200 1200,14 L1200,703 L0,703 Z" fill="url(#panelFade)"/>
    </svg>

    <div class="brand">
      <span class="brand__name">Pathbloom Counseling</span>
    </div>

    <div class="details">
      <h1 class="details__name">Marcus T. Whitfield, Ph.D.</h1>
      <p class="details__titles">Licensed Clinical Psychologist<br>Integrative Health Coach</p>
      <p class="details__address">4812 Ferndale Pkwy NW<span class="sep">•</span>Suite 730<span class="sep sep--lime">•</span>Duluth, GA 30096</p>
      <p class="details__numbers">
        <span class="number"><span class="number__badge">P</span>770.555.0142</span>
        <span class="number"><span class="number__badge">F</span>770.555.0186</span>
      </p>
      <p class="details__online">drmarcuswhitfield@kelvora.com<br>pathbloomcounseling.com</p>
    </div>
  </div>
</body>
</html>
```